Logo Design - Wine Range

Hello Designers,
We need a graphic design for a new logo for a wine range that we are releasing in coming months and are wanting to design a logo that reflects the name in a unique and creative way.
The Name is HERON GLEN.
We are really wanting the Logo/label to have a visual element which in a quick glance it is visually symbolic and one to remember.
Brief
A )Label with be 10 cm length and 9cm width, wanting picture to be about 5cm in Length. Information on the front label needs to be Name - Heron Glen
B) Looking for BRIGHT AND BOLD colours that attract and relate to Australian Nature. Can also include Falcon Bird but not necessary.
The designer who is selected as winner will need to create a label in order to complete the project. Goodluck :)
Thank you for your interest, looking forward to reviewing designs soon.
Updates
Label with be 10 cm length and 9cm width, wanting picture to be about 5cm in Length. Information on the front label needs to be Name - Heron Glen
have attached a colour palette of Australian Nature for an idea of colour.
Target Market(s)
Age group 18+
Industry/Entity Type
Graphic Design
Requirements
Must have
- Must include a graphic design not just words
Nice to have
- Unique and modern touch, If using Falcon would like the bird to be whole, Australian Nature. Rocks, waterfalls... the sky is the limit really , goodluck

```html
<!DOCTYPE html>
<html lang="en">
<head>
<meta charset="utf-8">
<title>Heron Glen – Merlot Label</title>
<link href="https://fonts.googleapis.com/css2?family=Oswald:wght@400;700&display=swap" rel="stylesheet">
<style>
  :root {
    --page: #ffffff;
    --sky-light: #dfe3df;
    --sky-mid: #a9b3a8;
    --foliage: #6f7c68;
    --cyan: #17b3c9;
    --orange: #f15a2b;
    --red: #d7252f;
    --paper: #f7f4f0;
    --white: #ffffff;
  }
  html, body {
    margin: 0;
    width: 802px;
    height: 1200px;
    overflow: hidden;
    background: var(--page);
  }
  .canvas {
    position: relative;
    width: 802px;
    height: 1200px;
  }
  .label {
    position: absolute;
    left: 41px;
    top: 320px;
    width: 720px;
    height: 560px;
    overflow: hidden;
    box-shadow: 0 2px 10px rgba(0,0,0,0.12);
  }
  .label__art {
    position: absolute;
    inset: 0;
    width: 720px;
    height: 560px;
  }
  .label__name {
    position: absolute;
    left: 44px;
    top: 458px;
    font-family: "Oswald", sans-serif;
    font-weight: 700;
    font-size: 42px;
    line-height: 1;
    letter-spacing: 4px;
    color: var(--white);
    white-space: nowrap;
  }
  .label__variety {
    position: absolute;
    left: 520px;
    top: 300px;
    font-family: "Oswald", sans-serif;
    font-weight: 400;
    font-size: 34px;
    color: var(--white);
    transform: rotate(-90deg);
    transform-origin: left top;
    letter-spacing: 1px;
  }
  .label__vintage {
    position: absolute;
    left: 560px;
    top: 300px;
    font-family: "Oswald", sans-serif;
    font-weight: 700;
    font-size: 150px;
    line-height: 1;
    color: var(--white);
    transform: rotate(-8deg);
  }
  .label__origin {
    position: absolute;
    left: 300px;
    top: 512px;
    font-family: "Oswald", sans-serif;
    font-size: 18px;
    letter-spacing: 3px;
    color: var(--red);
    transform: rotate(-4deg);
  }
</style>
</head>
<body>
<div class="canvas">
  <div class="label">
    <svg class="label__art" viewBox="0 0 720 560" xmlns="http://www.w3.org/2000/svg">
      <defs>
        <linearGradient id="photoTone" x1="0" y1="0" x2="0.6" y2="1">
          <stop offset="0" stop-color="var(--sky-light)"/>
          <stop offset="0.55" stop-color="var(--sky-mid)"/>
          <stop offset="1" stop-color="var(--foliage)"/>
        </linearGradient>
      </defs>
      <rect class="label__photo" x="0" y="0" width="720" height="560" fill="url(#photoTone)" role="img" aria-label="Photograph of a bird of prey with spread wings flying over misty gum trees"/>
      <polygon class="band band--cyan" points="0,380 720,200 720,280 0,470" fill="var(--cyan)"/>
      <polygon class="band band--orange" points="0,470 720,280 720,480 0,530" fill="var(--orange)"/>
      <polygon class="band band--red" points="540,325 720,280 720,480 540,494" fill="var(--red)"/>
      <polygon class="band band--paper" points="0,530 720,480 720,560 0,560" fill="var(--paper)"/>
    </svg>
    <div class="label__name">HERON GLEN</div>
    <div class="label__variety">merlot</div>
    <div class="label__vintage">11</div>
    <div class="label__origin">AUSTRALIA WINE</div>
  </div>
</div>
</body>
</html>
```